Bilingual school website redesign

The website oruvabilingualschool.example needs a new design

It is a private school from pre kinder to third grade

They teach Spanish and English

In the same website there is a section where teachers and parents interact
Updates

Reason: We are still waiting for approval from the school's teachers.

Target Market(s)

Mostly students' parents

Industry/Entity Type

Education

Number of Pages Required

3 page

Font styles to use
Sans Serif

Requirements
Must have
• Photo gallery
• Responsive design

```html
<!DOCTYPE html>
<html lang="en">
<head>
<meta charset="utf-8">
<title>Oruva Bilingual School</title>
<link href="https://fonts.googleapis.com/css2?family=Open+Sans:wght@400;600;700&family=Merriweather:wght@400;700&display=swap" rel="stylesheet">
<style>
:root{
  --navy:#1f2f8f;
  --blue:#2650b8;
  --blue-mid:#3a6fd0;
  --purple:#3d1f7a;
  --pink:#e86a8a;
  --ink:#333744;
  --muted:#7a7f8c;
  --line:#e3e5ec;
  --pale:#f4f5f8;
  --white:#ffffff;
}
*{box-sizing:border-box;margin:0;padding:0}
html,body{width:771px;height:1200px;overflow:hidden}
body{font-family:"Open Sans",Arial,sans-serif;color:var(--ink);background:var(--white);font-size:7px;line-height:1.5}
h2,h3{font-family:"Merriweather",Georgia,serif;font-weight:700}
.topbar{height:12px;background:var(--navy);color:#cfd6f5;font-size:5px;padding:3px 40px}
.header{height:63px;display:flex;align-items:center;justify-content:space-between;padding:0 40px;border-bottom:1px solid var(--line)}
.brand{display:flex;align-items:center;gap:6px;color:var(--navy);font-weight:700;font-size:10px}
.brand-dot{width:18px;height:18px;border-radius:50%;background:var(--navy)}
.nav{display:flex;gap:16px;font-size:6.5px;font-weight:600;color:var(--ink)}
.hero{height:203px;position:relative;background:var(--blue)}
.hero-photo{position:absolute;left:250px;top:0;right:0;bottom:0;background:linear-gradient(100deg,#3a6fd0 0%,#c9a98a 30%,#e8c9ae 60%,#9fb9d8 100%)}
.hero-text{position:absolute;left:40px;top:22px;width:200px;color:var(--white);font-size:6.5px;line-height:1.65}
.welcome{height:52px;display:flex;align-items:center;justify-content:space-between;padding:0 40px;border-bottom:1px solid var(--line)}
.welcome p{width:430px;color:var(--muted);font-size:6px}
.welcome b{color:var(--navy)}
.call{color:var(--navy);font-size:7px;font-weight:600}
.call strong{display:block;font-size:17px;font-weight:700;color:var(--blue)}
.services{height:318px;padding:20px 40px 0;text-align:center}
.services h2{font-size:14px;color:var(--navy)}
.sub{color:var(--muted);font-size:6px;margin:4px 0 18px}
.cards{display:flex;justify-content:space-between;padding:0 46px}
.card{width:120px}
.card-photo{width:100px;height:100px;border-radius:50%;margin:0 auto;border:3px solid var(--line)}
.card h3{font-size:9px;color:var(--navy);margin:8px 0 4px}
.card p{color:var(--muted);font-size:5.8px}
.btn{display:inline-block;background:var(--purple);color:var(--white);font-size:6px;font-weight:600;padding:5px 14px;margin-top:9px}
.why{height:122px;background:var(--blue);color:var(--white);text-align:center;padding:26px 110px 0}
.why h2{font-size:14px;margin-bottom:10px}
.why p{font-size:6px;color:#dbe4fb}
.cols{height:215px;display:flex;gap:24px;padding:28px 40px 0}
.col{flex:1}
.col h3{font-size:10px;color:var(--navy);margin-bottom:10px}
.event{display:flex;gap:8px;margin-bottom:10px}
.date{font-family:"Merriweather",Georgia,serif;font-size:12px;color:var(--navy);font-weight:700;width:18px}
.event b{display:block;font-size:6.5px}
.event span{color:var(--muted);font-size:5.8px}
.quote{border:1px solid var(--line);padding:10px;color:var(--muted);font-size:6px;height:90px}
.quote b{color:var(--navy);display:block;margin-bottom:4px}
.form{display:grid;grid-template-columns:1fr 1fr;gap:6px}
.form span{border:1px solid var(--line);padding:5px;color:var(--muted);font-size:5.8px}
.form .msg{grid-column:1/3;height:46px}
.center{text-align:center}
.happy{height:180px;text-align:center;padding:14px 80px 0;background:var(--pale)}
.happy h2{font-size:16px;color:var(--pink);font-weight:400}
.happy .text{color:var(--muted);font-size:6px;margin-top:6px}
.avatar{width:30px;height:30px;border-radius:50%;background:#c8ccd8;margin:10px auto 4px}
.happy strong{display:block;font-size:7px;color:var(--ink)}
.happy small{font-size:5.5px;color:var(--muted)}
.footer{height:35px;background:var(--navy);color:#cfd6f5;font-size:5.5px;display:flex;justify-content:space-between;align-items:center;padding:0 40px}
</style>
</head>
<body>
<div class="topbar">oruvabilingualschool.example</div>
<header class="header">
  <div class="brand"><span class="brand-dot"></span>Oruva Bilingual School</div>
  <nav class="nav"><span>Home</span><span>Our School</span><span>News</span><span>Activities</span><span>Children Resources</span><span>Contact Us</span></nav>
</header>
<section class="hero">
  <div class="hero-photo" role="img" aria-label="Photo of smiling young students with their teacher in a classroom"></div>
  <p class="hero-text">Welcome to a school where children learn in two languages every day. Our small classes, caring teachers and playful lessons help each child grow with confidence in Spanish and English from pre kinder to third grade.</p>
</section>
<section class="welcome">
  <p><b>Welcome:</b> Every child is welcome here. We build strong bilingual readers, curious thinkers and kind classmates through daily play and practice.</p>
  <div class="call">Call today for your FREE assessment<strong>4410-7726</strong></div>
</section>
<section class="services">
  <h2>What Do We Do</h2>
  <p class="sub">We plan each day around language, numbers and discovery so children enjoy learning.</p>
  <div class="cards">
    <div class="card"><div class="card-photo" role="img" aria-label="Photo of a child writing on a chalkboard" style="background:#5b6a5e"></div><h3>English</h3><p>Stories, songs and reading games that grow vocabulary and clear speaking every day.</p><span class="btn">View More</span></div>
    <div class="card"><div class="card-photo" role="img" aria-label="Photo of maths worksheets and a pencil" style="background:#d9dde3"></div><h3>Maths</h3><p>Counting, shapes and puzzles taught with hands-on materials and friendly small group work.</p><span class="btn">View More</span></div>
    <div class="card"><div class="card-photo" role="img" aria-label="Photo of children doing a science activity" style="background:#c9a98a"></div><h3>Science</h3><p>Simple experiments and nature walks that spark questions and careful observation in class.</p><span class="btn">View More</span></div>
    <div class="card"><div class="card-photo" role="img" aria-label="Photo of a tutor helping a student" style="background:#a88f7c"></div><h3>Tutors</h3><p>One to one support in Spanish and English for children who need extra practice.</p><span class="btn">View More</span></div>
  </div>
</section>
<section class="why">
  <h2>Why Choose Us</h2>
  <p>Our teachers are fluent in both languages and know every child by name. Classes stay small, families are part of daily school life, and our teacher and parent area keeps everyone informed about homework, events and progress.</p>
</section>
<section class="cols">
  <div class="col">
    <h3>Class Timings</h3>
    <div class="event"><span class="date">01</span><div><b>English Language and Grammar Class</b><span>Mon to Fri, 8:00 am – 9:30 am</span></div></div>
    <div class="event"><span class="date">04</span><div><b>Maths Club</b><span>Tue and Thu, 10:00 am – 11:00 am</span></div></div>
    <div class="event"><span class="date">05</span><div><b>Science Club</b><span>Wed and Fri, 11:30 am – 12:30 pm</span></div></div>
    <div class="center"><span class="btn">View More</span></div>
  </div>
  <div class="col">
    <h3>From Our Blog</h3>
    <div class="quote"><b>Tips for reading at home</b>Read together for ten minutes a day, switch languages each night, and let your child choose the book. Small habits build lasting bilingual readers.</div>
    <div class="center"><span class="btn">View More</span></div>
  </div>
  <div class="col">
    <h3>Contact Us</h3>
    <div class="form"><span>Name</span><span>Email</span><span>Phone</span><span>Subject</span><span class="msg">Message</span></div>
    <div class="center"><span class="btn">View More</span></div>
  </div>
</section>
<section class="happy">
  <h2>Happy Students</h2>
  <p class="text">Families share what a day at our school means to them.</p>
  <p class="text">Our daughter started in pre kinder speaking only English. Two years later she reads in both languages, sings Spanish songs at home and cannot wait to see her teachers each morning. The staff keep us updated and always make time to talk with parents.</p>
  <div class="avatar" role="img" aria-label="Parent portrait"></div>
  <strong>Lena Marsh</strong>
  <small>Parent of a second grader</small>
</section>
<footer class="footer"><span>© Oruva Bilingual School. All rights reserved.</span><span>Terms of Use | Privacy Policy | Sitemap</span></footer>
</body>
</html>
```